BRIM Exterior Coatings

double sided. the front i want the name of the business each word on a new line with the BRIM being bigger. id like teal, black and white colors. the back i want my contact info. Flat, no gloss. Something professional and I want to feel the letters bump put of the card. if possible maybe a paint sprayer in corner. not a car paint spray. (no tank on top of gun)
no vehicle paint sprayers. that means no tank on top of the gun. doesn't have to have a sprayer. black/dark background on the front. white back ground on back with info

```html
<!DOCTYPE html>
<html lang="en">
<head>
<meta charset="UTF-8">
<title>BRIM Exterior Coatings – Business Card</title>
<link href="https://fonts.googleapis.com/css2?family=Open+Sans:wght@400;600;700;800&display=swap" rel="stylesheet">
<style>
  :root {
    --teal: #2a9fa3;
    --ink: #1b1b1b;
    --black: #050505;
    --white: #ffffff;
    --stage: #3a3a3c;
    --art-light: #4a4a4c;
    --art-dark: #141414;
  }
  * { margin: 0; padding: 0; box-sizing: border-box; }
  html, body {
    width: 1200px;
    height: 900px;
    overflow: hidden;
    background: var(--stage);
    font-family: "Open Sans", Arial, sans-serif;
  }
  .stage {
    position: relative;
    width: 1200px;
    height: 900px;
  }
  .card {
    position: absolute;
    left: 250px;
    width: 700px;
    height: 400px;
    overflow: hidden;
    box-shadow: 0 10px 28px rgba(0,0,0,0.45);
  }
  /* Front */
  .card-front {
    top: 40px;
    background: var(--black);
  }
  .front-brand {
    position: absolute;
    left: 110px;
    top: 130px;
    width: 330px;
    text-align: center;
  }
  .front-name {
    font-weight: 800;
    font-size: 100px;
    line-height: 1;
    letter-spacing: 2px;
    color: var(--white);
  }
  .front-tagline {
    margin-top: 10px;
    font-weight: 400;
    font-size: 21px;
    letter-spacing: 2px;
    color: var(--teal);
    white-space: nowrap;
  }
  .sprayer-art {
    position: absolute;
    left: 470px;
    top: 50px;
    width: 180px;
    height: 240px;
    border-radius: 6px;
    background: radial-gradient(circle at 55% 45%, var(--art-light), var(--art-dark));
  }
  /* Back */
  .card-back {
    top: 460px;
    background: var(--white);
  }
  .back-name {
    position: absolute;
    left: 30px;
    top: 135px;
    width: 300px;
    text-align: center;
    font-weight: 800;
    font-size: 100px;
    line-height: 1;
    letter-spacing: 2px;
    color: var(--ink);
  }
  .divider {
    position: absolute;
    left: 355px;
    top: 90px;
    width: 2px;
    height: 220px;
    background: var(--ink);
  }
  .contact {
    position: absolute;
    left: 385px;
    top: 96px;
    width: 295px;
    color: var(--ink);
  }
  .person-name {
    font-weight: 700;
    font-size: 30px;
    line-height: 1.1;
    letter-spacing: 0.5px;
    color: var(--teal);
    text-transform: uppercase;
    white-space: nowrap;
  }
  .person-role {
    font-size: 20px;
    line-height: 1.2;
    margin-bottom: 14px;
  }
  .address {
    font-size: 21px;
    line-height: 1.25;
    margin-bottom: 12px;
  }
  .contact-list { list-style: none; }
  .contact-item {
    display: flex;
    align-items: center;
    gap: 12px;
    font-size: 21px;
    line-height: 1.3;
    white-space: nowrap;
  }
  .contact-icon { width: 18px; height: 18px; flex: none; }
  .contact-icon * { fill: var(--teal); }
</style>
</head>
<body>
<main class="stage">

  <section class="card card-front" aria-label="Card front">
    <div class="front-brand">
      <div class="front-name">BRIM</div>
      <div class="front-tagline">EXTERIOR COATINGS</div>
    </div>
    <div class="sprayer-art" role="img" aria-label="White line drawing of a paint spray gun with a fine spray mist"></div>
  </section>

  <section class="card card-back" aria-label="Card back">
    <div class="back-name">BRIM</div>
    <div class="divider"></div>
    <div class="contact">
      <h1 class="person-name">Daniel Reyes</h1>
      <p class="person-role">Manager</p>
      <p class="address">Your address, city<br>state, ZIP 0000</p>
      <ul class="contact-list">
        <li class="contact-item">
          <svg class="contact-icon" viewBox="0 0 24 24" aria-hidden="true"><path d="M6.6 10.8a15.1 15.1 0 0 0 6.6 6.6l2.2-2.2c.3-.3.7-.4 1-.2 1.1.4 2.3.6 3.6.6.6 0 1 .4 1 1V20c0 .6-.4 1-1 1C10.6 21 3 13.4 3 4c0-.6.4-1 1-1h3.5c.6 0 1 .4 1 1 0 1.3.2 2.5.6 3.6.1.3 0 .7-.2 1z"/></svg>
          <span>555-014-2100</span>
        </li>
        <li class="contact-item">
          <svg class="contact-icon" viewBox="0 0 24 24" aria-hidden="true"><path d="M2 5h20v14H2zM4 7v.4l8 5.2 8-5.2V7zm0 2.8V17h16V9.8l-8 5.2z"/></svg>
          <span>hello@brimcoatings.com</span>
        </li>
        <li class="contact-item">
          <svg class="contact-icon" viewBox="0 0 24 24" aria-hidden="true"><path d="M12 2a10 10 0 1 0 0 20 10 10 0 0 0 0-20zm6.9 6h-3a15.6 15.6 0 0 0-1.3-3.9A8 8 0 0 1 18.9 8zM12 4c.8 1.2 1.5 2.5 1.9 4h-3.8c.4-1.5 1.1-2.8 1.900-4zM4.3 14a8 8 0 0 1 0-4h3.4a16.5 16.5 0 0 0 0 4zm.8 2h3a15.6 15.6 0 0 0 1.3 3.9A8 8 0 0 1 5.1 16zM8 8H5.1a8 8 0 0 1 4.3-3.9C8.8 5.3 8.4 6.6 8 8zm4 12c-.8-1.2-1.5-2.5-1.9-4h3.8c-.4 1.5-1.1 2.8-1.9 4zm2.3-6H9.7a14.7 14.7 0 0 1 0-4h4.6a14.7 14.7 0 0 1 0 4zm.3 5.9c.6-1.2 1-2.5 1.3-3.9h3a8 8 0 0 1-4.3 3.9zm1.7-5.9a16.5 16.5 0 0 0 0-4h3.4a8 8 0 0 1 0 4z"/></svg>
          <span>www.brimcoatings.com</span>
        </li>
      </ul>
    </div>
  </section>

</main>
</body>
</html>
```